TIME BAR Design Project

DESIGN: TIME LAPSE BAR

We are looking for a fresh design for a time lapse bar which would appear on screen during an exercise video.

Please see a quick example attached. We would like it to be created in Photoshop or Illustrator, in layers. ( no after effects please).

We need a layer that would move to indicate the time passing.

We would like to manipulate the time as needed for various pieces.
Updates

Quick update:
please note the current bar in the sample picts was done in-house and is only intended to be a guide.  The bar does not have to resemble the sample. Thanks.

Target Market(s)

male /female 25-65 60% women.

Requirements
Must have
• Created in Photoshop or Illustrator.

Minimum 300DPI.

Please see that there is needs to be a place for the name of each exercise - this can appear and then fade out.
Nice to have
• -bar should match the mood of the set and colors.( see picts).

-bar CAN BE see-through so that the body's are seen behind it.
Should not have
• too high tech or masculine

too feminine

```html
<!DOCTYPE html>
<html lang="en">
<head>
<meta charset="utf-8">
<title>Time Lapse Bar</title>
<link rel="stylesheet" href="https://fonts.googleapis.com/css2?family=Nunito:wght@600;700&display=swap">
<style>
  :root {
    --letterbox: #000000;
    --wall-light: #efe6d8;
    --wall-warm: #e4d3bd;
    --trim-orange: #d9894a;
    --floor-light: #e8b77f;
    --floor-deep: #c98a4e;
    --bar-glass: rgba(255, 249, 241, 0.42);
    --bar-edge: rgba(255, 255, 255, 0.75);
    --label-fill: rgba(214, 128, 64, 0.92);
    --label-text: #ffffff;
    --track: rgba(80, 66, 54, 0.28);
    --progress-start: #e0894a;
    --progress-end: #6f8fc4;
    --tick: rgba(255, 255, 255, 0.85);
    --knob-fill: #ffffff;
    --knob-ring: #d6803f;
    --time-text: #3b2f25;
  }
  html, body {
    margin: 0;
    padding: 0;
    width: 1200px;
    height: 719px;
    overflow: hidden;
    background: var(--letterbox);
  }
  .screen {
    position: relative;
    width: 1200px;
    height: 719px;
    background: var(--letterbox);
    font-family: "Nunito", Arial, sans-serif;
  }
  .video-frame {
    position: absolute;
    left: 0;
    top: 15px;
    width: 1200px;
    height: 677px;
    background: linear-gradient(180deg,
      var(--wall-light) 0%,
      var(--wall-warm) 48%,
      var(--trim-orange) 53%,
      var(--floor-light) 56%,
      var(--floor-deep) 100%);
  }
  .time-bar {
    position: absolute;
    left: 187px;
    top: 618px;
    width: 804px;
    height: 40px;
    box-sizing: border-box;
    padding: 4px;
    display: flex;
    align-items: center;
    border-radius: 20px;
    background: var(--bar-glass);
    border: 1px solid var(--bar-edge);
    box-shadow: 0 2px 10px rgba(60, 40, 20, 0.18);
  }
  .exercise-name {
    flex: 0 0 196px;
    height: 30px;
    border-radius: 15px;
    background: var(--label-fill);
    color: var(--label-text);
    font-weight: 700;
    font-size: 15px;
    letter-spacing: 0.03em;
    line-height: 30px;
    text-align: center;
    white-space: nowrap;
  }
  .progress-area {
    position: relative;
    flex: 1 1 auto;
    height: 30px;
    margin: 0 18px;
  }
  .track {
    position: absolute;
    left: 0;
    right: 0;
    top: 12px;
    height: 6px;
    border-radius: 3px;
    background: var(--track);
  }
  .progress {
    position: absolute;
    left: 0;
    top: 12px;
    width: 21%;
    height: 6px;
    border-radius: 3px;
    background: linear-gradient(90deg, var(--progress-start), var(--progress-end));
  }
  .segment-tick {
    position: absolute;
    top: 11px;
    width: 2px;
    height: 8px;
    margin-left: -1px;
    border-radius: 1px;
    background: var(--tick);
  }
  .knob {
    position: absolute;
    left: 21%;
    top: 15px;
    width: 12px;
    height: 12px;
    margin: -9px 0 0 -9px;
    border-radius: 50%;
    background: var(--knob-fill);
    border: 3px solid var(--knob-ring);
    box-shadow: 0 1px 4px rgba(60, 40, 20, 0.3);
  }
  .time-readout {
    flex: 0 0 104px;
    padding-right: 12px;
    text-align: right;
    color: var(--time-text);
    font-weight: 600;
    font-size: 14px;
    white-space: nowrap;
  }
</style>
</head>
<body>
<main class="screen">
  <div class="video-frame" role="img" aria-label="Exercise video scene: an instructor and a trainer working out with resistance bands in a bright studio with a warm wooden floor"></div>

  <div class="time-bar" role="progressbar" aria-label="Workout time elapsed" aria-valuemin="0" aria-valuemax="100" aria-valuenow="21">
    <div class="exercise-name">Band Chest Pull</div>
    <div class="progress-area">
      <div class="track"></div>
      <div class="progress"></div>
      <span class="segment-tick" style="left:25%"></span>
      <span class="segment-tick" style="left:50%"></span>
      <span class="segment-tick" style="left:75%"></span>
      <div class="knob"></div>
    </div>
    <div class="time-readout">12:40 / 45:00</div>
  </div>
</main>
</body>
</html>
```